New design and build for natural product Velmarin nosespray

We are looking for a new design for an existing website.

Velmarin is a natural product. we have three types of products. Please have a look at the existing site: velmarin-example.com

We are looking for a natural look and feel. This because the products are 100 procent natural.

We would like to have the following site structure (rows) :
- Picture of a person in nature
- Packshot
- Tekst
- 4 blocks for the four nasal issues with pictures
- Tekst
- 3 blocks with pictures to explain experiences from others.
- I think a need an extra white block with tekst (like this example ‘let your dreams come true’

Please have a look at the attached pdf.
page 2 is a idea where the site structure is important.
page 3 is an existing folder. Idear is to keep the folder look and feel in line with the new site design.
page 4-5-6 Element that are posible.
page 7 design that is too much.

Beside the home page I would like to have a template for the sales page.

The existing site has a large woocommerce customer database. This must stay available.
I have a staging site available where you can build the site. From here we can export and import the new disgn to the production site.

Please make the site in Divi

Requirements
Must have
• Home page and sales page
Nice to have
• see pdf

```html
<!DOCTYPE html>
<html lang="en">
<head>
<meta charset="utf-8">
<title>Velmarin – natural nasal spray</title>
<link href="https://fonts.googleapis.com/css2?family=Jost:wght@400;500;600&family=Open+Sans:wght@400;600&family=Montserrat:wght@500;600&family=Pathway+Gothic+One&display=swap" rel="stylesheet">
<style>
:root{
  --red:#e0121b;
  --red-dark:#c80f17;
  --ink:#222222;
  --text:#444444;
  --grey-btn:#4a4a4a;
  --pink:#fdeeee;
  --topbar:#3b3b3b;
  --footer:#232323;
  --white:#ffffff;
}
*{box-sizing:border-box;margin:0;padding:0}
html,body{width:1200px;height:4021px;overflow:hidden}
body{background:var(--white);font-family:"Open Sans",sans-serif;color:var(--text);position:relative}
.abs{position:absolute}
h1,h2,h3,h4{font-family:"Jost",sans-serif;font-weight:500;color:var(--ink)}
.accent{color:var(--red)}
.btn{display:inline-flex;align-items:center;justify-content:center;border-radius:20px;font-family:"Montserrat",sans-serif;font-weight:600;font-size:12px;color:var(--white);height:38px;padding:0 15px;text-transform:uppercase}
.btn-red{background:var(--red)}
.btn-grey{background:var(--grey-btn)}

/* top bar */
.topbar{top:0;left:0;width:1200px;height:35px;background:var(--topbar);color:#eee;font-size:11.5px}
.topbar span{position:absolute;top:10px}
/* header */
.header{top:35px;left:0;width:1200px;height:121px;background:var(--white)}
.logo{position:absolute;left:172px;top:34px;font-family:"Jost",sans-serif;font-weight:600;font-size:36px;color:var(--topbar);letter-spacing:.5px}
.nav{position:absolute;left:441px;top:52px;display:flex;gap:20px;font-family:"Montserrat",sans-serif;font-weight:600;font-size:12.5px;color:var(--ink)}
.shop{position:absolute;left:944px;top:48px;width:84px;height:40px;border-radius:20px;background:var(--red);color:var(--white);font-family:"Montserrat",sans-serif;font-weight:600;font-size:13px;display:flex;align-items:center;justify-content:center}

/* hero */
.hero{top:156px;left:0;width:1200px;height:671px;overflow:hidden}
.hero-photo{position:absolute;inset:0;background:radial-gradient(ellipse at 72% 45%,#8a8a78 0,#6f8a4e 22%,transparent 40%),linear-gradient(160deg,#5d8a33 0%,#8db554 35%,#4f7a2a 70%,#3f6322 100%)}
.hero-title{position:absolute;left:172px;top:106px;font-family:"Jost",sans-serif;font-weight:600;font-size:47px;line-height:62px;color:var(--white);letter-spacing:-1px;text-shadow:0 2px 6px rgba(0,0,0,.35)}
.hero .btn{position:absolute;left:172px;top:252px;background:var(--white);color:var(--ink);height:50px;border-radius:26px;padding:0 16px;font-size:15px;font-weight:500}
.hero-wave{position:absolute;left:0;bottom:0}

/* product */
.packshot{left:203px;top:905px;width:242px;height:298px;border-radius:6px;background:linear-gradient(90deg,#e23a2f 0,#d8261f 45%,#f4f1ec 62%,#e9d8b6 100%)}
.product-text{left:528px;top:898px;width:500px}
.product-text h2{font-size:29px;font-weight:500;letter-spacing:-.3px}
.product-text p{margin-top:18px;font-size:12px;line-height:24px}
.checks{list-style:none;margin-top:12px}
.checks li{font-family:"Pathway Gothic One",sans-serif;font-size:17px;line-height:30px;color:var(--ink);display:flex;align-items:center;gap:10px}

/* complaints */
.pink-top{left:0;top:1225px}
.complaints{left:0;top:1385px;width:1200px;height:687px;background:var(--pink)}
.center-title{text-align:center;font-size:29px;letter-spacing:-.3px}
.complaints h2{position:absolute;top:70px;width:100%}
.complaints .intro{position:absolute;top:124px;left:180px;width:840px;text-align:center;font-size:12px;line-height:24px}
.card{position:absolute;background:var(--white);border-radius:22px;box-shadow:0 4px 14px rgba(0,0,0,.08);text-align:center}
.card-photo{position:absolute;left:10px;top:10px;border-radius:18px}
.card h3{position:absolute;left:0;width:100%;font-size:16px;font-weight:500;text-transform:uppercase}
.card p{position:absolute;font-size:11px;line-height:20px}
.card .btn{position:absolute;left:50%;transform:translateX(-50%)}
.complaint{top:249px;width:212px;height:341px}
.complaint .card-photo{width:192px;height:172px}
.complaint h3{top:192px}
.complaint p{top:218px;left:14px;width:184px}
.complaint .btn{top:279px}

/* band */
.band{left:0;top:2072px;width:1200px;height:152px;background:var(--red);color:var(--white);overflow:hidden}
.band h2{position:absolute;left:172px;top:44px;color:var(--white);font-size:27px;font-weight:500}
.band p{position:absolute;left:172px;top:82px;font-family:"Jost",sans-serif;font-size:19px}
.band-deco{position:absolute;left:650px;top:0;width:378px;height:152px;background:linear-gradient(90deg,rgba(255,255,255,.12),rgba(255,255,255,.22))}

/* tips */
.tips-title{left:0;top:2296px;width:1200px}
.tip{top:2392px;width:265px;height:401px}
.tip .card-photo{width:245px;height:173px;overflow:hidden}
.posted{position:absolute;right:0;bottom:0;background:var(--white);padding:6px 14px 0;font-size:11.5px;color:var(--text);border-top-left-radius:6px}
.tip h3{top:210px;font-size:13.5px;line-height:22px;padding:0 28px}
.tip p{top:260px;left:18px;width:229px;font-size:10.5px;line-height:20px}
.tip .btn{top:331px}

/* dreams */
.pink-top-2{left:0;top:2805px}
.dreams{left:0;top:2975px;width:1200px;height:420px;background:var(--pink)}
.flower{position:absolute;left:84px;top:68px;width:310px;height:382px;border-radius:40% 40% 30% 30%;background:radial-gradient(circle at 55% 30%,rgba(0,0,0,.06),rgba(0,0,0,.02) 60%,transparent 70%)}
.dreams h2{position:absolute;left:462px;top:112px;font-size:29px;letter-spacing:-.3px}
.dreams p{position:absolute;left:462px;top:163px;width:568px;font-size:12px;line-height:24px}
.dreams .btn{position:absolute;left:462px;top:289px}

/* footer */
.footer-wave{left:0;top:3340px}
.footer{left:0;top:3525px;width:1200px;height:496px;background:var(--footer);color:#dcdcdc}
.fcol{position:absolute;top:112px;font-size:12.5px;line-height:24px}
.fcol h4{color:var(--white);font-size:17px;font-weight:400;margin-bottom:8px;text-transform:uppercase;letter-spacing:-.2px}
.footer .rule{position:absolute;left:172px;top:393px;width:856px;height:1px;background:#8a8a8a}
.footer .copy{position:absolute;top:435px;width:100%;text-align:center;font-size:13px;color:var(--white)}
</style>
</head>
<body>

<div class="abs topbar">
  <span style="left:172px">Ordered on working days shipped the next day.</span>
  <span style="left:518px">Shipping costs 2.95 euros in NL</span>
  <span style="left:843px">&#10142; login</span>
  <span style="left:902px">&#128274; shopping cart / €0,00</span>
</div>

<header class="abs header">
  <div class="logo">Velmarin</div>
  <nav class="nav"><span>HOME</span><span>PRODUCT</span><span>RESEARCH</span><span>EXPERIENCES</span><span>TIPS/INFO</span><span>CONTACT</span></nav>
  <div class="shop">SHOP</div>
</header>

<section class="abs hero">
  <div class="hero-photo" role="img" aria-label="Woman meditating cross-legged on a rock in green nature"></div>
  <h1 class="hero-title">WEER VRIJ ADEMEN<br>DOOR DE NEUAS</h1>
  <span class="btn">READ MORE</span>
  <svg class="hero-wave" width="1200" height="230" viewBox="0 0 1200 230">
    <path d="M0 125 C200 55 330 45 460 90 C600 140 690 215 860 212 C1000 210 1110 135 1200 78 L1200 230 L0 230 Z" fill="var(--red)"/>
    <path d="M0 162 C200 80 330 60 460 105 C600 160 690 232 860 230 C1000 232 1110 180 1200 128 L1200 230 L0 230 Z" fill="var(--white)"/>
  </svg>
</section>

<div class="abs packshot" role="img" aria-label="Velmarin nasal spray box and bottle packshot"></div>
<div class="abs product-text">
  <h2>100% NATURAL <span class="accent">NASAL SPRAY</span></h2>
  <p>Suffering from a runny nose or chronic cold? Velmarin helps you to breathe freely through the nose and reduces sensitivity to allergens. Velmarin has been proven effective and contains only natural ingredients, such as salt, xylitol and capsaicin.</p>
  <ul class="checks">
    <li><svg width="12" height="10" viewBox="0 0 12 10"><path d="M1 5 L4.5 8.5 L11 1" stroke="var(--red)" stroke-width="2.4" fill="none"/></svg>100% natural</li>
    <li><svg width="12" height="10" viewBox="0 0 12 10"><path d="M1 5 L4.5 8.5 L11 1" stroke="var(--red)" stroke-width="2.4" fill="none"/></svg>Proven effective</li>
    <li><svg width="12" height="10" viewBox="0 0 12 10"><path d="M1 5 L4.5 8.5 L11 1" stroke="var(--red)" stroke-width="2.4" fill="none"/></svg>Long-term use</li>
    <li><svg width="12" height="10" viewBox="0 0 12 10"><path d="M1 5 L4.5 8.5 L11 1" stroke="var(--red)" stroke-width="2.4" fill="none"/></svg>Recommended by ENT doctors</li>
    <li><svg width="12" height="10" viewBox="0 0 12 10"><path d="M1 5 L4.5 8.5 L11 1" stroke="var(--red)" stroke-width="2.4" fill="none"/></svg>Against runny nose, stuffy nose &amp; chronic colds</li>
    <li><svg width="12" height="10" viewBox="0 0 12 10"><path d="M1 5 L4.5 8.5 L11 1" stroke="var(--red)" stroke-width="2.4" fill="none"/></svg>Naturally strengthens your nasal mucosa</li>
  </ul>
</div>

<svg class="abs pink-top" width="1200" height="162" viewBox="0 0 1200 162">
  <path d="M0 160 C120 90 240 70 360 80 C520 95 650 170 820 150 C990 130 1100 60 1200 0 L1200 162 L0 162 Z" fill="var(--red)"/>
  <path d="M0 162 C120 110 240 95 360 100 C520 110 650 180 820 162 C990 145 1100 95 1200 40 L1200 162 Z" fill="var(--pink)"/>
</svg>

<section class="abs complaints">
  <h2 class="center-title">CHRONIC <span class="accent">NASAL COMPLAINTS</span></h2>
  <p class="intro">Velmarin nasal spray is especially effective for chronic nasal complaints. The formulas help to breathe more freely through the nose and provide relief from blocked sinuses and forehead pressure. These conditions can have various causes. Read the articles below to find out what is bothering you and what you can do to feel better quickly.</p>

  <article class="card complaint" style="left:150px">
    <div class="card-photo" role="img" aria-label="Woman under a blanket blowing her stuffy nose" style="background:linear-gradient(135deg,#cfd3d8,#8e96a0)"></div>
    <h3>Stuffy nose</h3>
    <p>A stuffy nose is usually caused by a cold.</p>
    <span class="btn btn-red">READ MORE</span>
  </article>
  <article class="card complaint" style="left:379px">
    <div class="card-photo" role="img" aria-label="Woman in red sweater with a tissue for a running nose" style="background:linear-gradient(135deg,#8a8f96,#c23a3a)"></div>
    <h3>Running nose</h3>
    <p>A stuffy nose is usually caused by a cold.</p>
    <span class="btn btn-grey">READ MORE</span>
  </article>
  <article class="card complaint" style="left:609px">
    <div class="card-photo" role="img" aria-label="Woman pressing the bridge of her nose with sinus pain" style="background:linear-gradient(135deg,#e6e3df,#8d7766)"></div>
    <h3>Sinusitis</h3>
    <p>A stuffy nose is usually caused by a cold.</p>
    <span class="btn btn-grey">READ MORE</span>
  </article>
  <article class="card complaint" style="left:839px">
    <div class="card-photo" role="img" aria-label="Man using a nasal spray" style="background:linear-gradient(135deg,#b3aca3,#6f6a64)"></div>
    <h3>Nasal spray addiction</h3>
    <p>A stuffy nose is usually caused by a cold.</p>
    <span class="btn btn-grey">READ MORE</span>
  </article>
</section>

<section class="abs band">
  <h2>WIL JE MEER LEZEN OVER</h2>
  <p>ervaringen van anderen?</p>
  <div class="band-deco" role="img" aria-label="Line drawn flower decorations"></div>
</section>

<h2 class="abs center-title tips-title">TIPS AND <span class="accent">EXPERIENCES</span></h2>

<article class="abs card tip" style="left:172px">
  <div class="card-photo" role="img" aria-label="Man holding his head with a headache in a kitchen" style="background:linear-gradient(135deg,#d9d6d0,#6b6560 70%,#3f6b43)"><span class="posted">Posted on 19/12/2017</span></div>
  <h3>HEADACHE DUE TO STUFFY NOSE</h3>
  <p>For years I have suffered from a stuffy nose and persistent headaches because I have ab normalities in the septum of my nose.</p>
  <span class="btn btn-red">READ MORE</span>
</article>
<article class="abs card tip" style="left:468px">
  <div class="card-photo" role="img" aria-label="Woman in a knitted hat sneezing into a tissue" style="background:linear-gradient(135deg,#cfc6c2,#9b3b45)"><span class="posted">Posted on 19/12/2017</span></div>
  <h3>SNEEZING, MY NOSE REACTS TO EVERYTHING.</h3>
  <p>I have a chronic (idiopathic) cold. When a man with strong aftershave walks past me, I imme diately start to sneeze</p>
  <span class="btn btn-grey">READ MORE</span>
</article>
<article class="abs card tip" style="left:763px">
  <div class="card-photo" role="img" aria-label="Woman with a scarf and cold under an air conditioner" style="background:linear-gradient(135deg,#e8ecf0,#6f8aa8)"><span class="posted">Posted on 20/12/2019</span></div>
  <h3>COLD DUE TO AIR CONDITIONING</h3>
  <p>What a wonderfully warm summer we have. Although nature is visibly bothered by it, I can enjoy it. During the day maybe a little too</p>
  <span class="btn btn-grey">READ MORE</span>
</article>

<svg class="abs pink-top-2" width="1200" height="172" viewBox="0 0 1200 172">
  <path d="M0 170 C120 90 220 60 360 70 C560 85 700 150 880 140 C1020 132 1120 60 1200 0 L1200 172 L0 172 Z" fill="var(--red)"/>
  <path d="M0 172 C120 110 220 88 360 92 C560 100 700 170 880 160 C1020 152 1120 95 1200 42 L1200 172 Z" fill="var(--pink)"/>
</svg>

<section class="abs dreams">
  <div class="flower" role="img" aria-label="Line illustration of a flower with leaves"></div>
  <h2>LET YOUR <span class="accent">DREAMS COME TRUE</span></h2>
  <p>Velmarin nasal spray is especially effective for chronic nasal complaints. The formulas help to breathe more freely through the nose and provide relief from blocked sinuses and forehead pressure. These conditions can have various causes. Read the articles below to find out what is bothering you and what you can do to feel better quickly.</p>
  <span class="btn btn-red">READ MORE</span>
</section>

<svg class="abs footer-wave" width="1200" height="190" viewBox="0 0 1200 190">
  <rect x="0" y="0" width="1200" height="60" fill="var(--pink)"/>
  <path d="M0 110 C150 150 280 160 420 125 C580 85 700 10 860 15 C1000 20 1100 100 1200 135 L1200 190 L0 190 Z" fill="var(--red)"/>
  <path d="M0 150 C150 180 280 185 420 160 C580 125 700 60 860 62 C1000 65 1100 140 1200 175 L1200 190 L0 190 Z" fill="var(--footer)"/>
</svg>

<footer class="abs footer">
  <div class="fcol" style="left:172px">
    <h4>Information</h4>
    Privacy declaration<br>Terms and Conditions Velmarin<br>Pregnancy<br>Instructions for use Velmarin<br>nasal spray
  </div>
  <div class="fcol" style="left:411px">
    <h4>Customer service</h4>
    Contact<br>Shop<br>Send order<br>Stores<br>Frequently Asked<br>Questions
  </div>
  <div class="fcol" style="left:621px">
    <h4>Contact</h4>
    Nasoria BV<br>(Note: this is not a sales address)<br>Lindelaan 12<br>1234 AB Amersfoort<br>+31 (0)20 -000 00 00<br>info@velmarin-example.nl<br>Chamber of Commerce: 12345678<br>VAT number: NL000.000.000B.01
  </div>
  <div class="fcol" style="left:894px">
    <h4>International</h4>
    France: velmarin-example.fr<br><br>England: velmarin-example.co.uk<br><br>Spain: velmarin-example.es
  </div>
  <div class="rule"></div>
  <div class="copy">Copyrights @ 2021 Velmarin. All Rights Reserved.</div>
</footer>

</body>
</html>
```